Health Care Company with Logo Needs Business Cards designed

We are a luxury behavioral health company looking for business cards design we already have a logo and are looking for someone to design a sophisticated luxurious looking business card. Please note that Card design should be captivating just like the logo and also encompass the logo color

Industry/Entity Type

Healthcare

Contact Information for Business Card

Logo,company name, tagline, my name and title, contact details, and physical address

```html
<!DOCTYPE html>
<html lang="en">
<head>
<meta charset="utf-8">
<title>Corven Behavioral Health — Business Card</title>
<link href="https://fonts.googleapis.com/css2?family=Roboto+Condensed:wght@500&family=Roboto:ital,wght@0,400;0,500;1,400&display=swap" rel="stylesheet">
<style>
  :root {
    --page: #2a2a2b;
    --card: #262627;
    --back-light: #5a5a5b;
    --back-mid: #2a2a2b;
    --back-dark: #0c0c0c;
    --purple: #7a3a93;
    --blue: #1a9ad6;
    --orange: #f0951f;
    --text: #e6e6e6;
  }
  * { margin: 0; padding: 0; box-sizing: border-box; }
  html, body { width: 1138px; height: 1200px; overflow: hidden; }
  body { background: var(--page); position: relative; font-family: "Roboto", Arial, sans-serif; }

  .card {
    position: absolute;
    width: 376px;
    height: 620px;
    border-radius: 16px;
    overflow: hidden;
  }
  .card--back {
    left: 186px; top: 302px;
    background:
      radial-gradient(ellipse 70% 45% at 45% 18%, rgba(120,120,121,0.55) 0%, rgba(120,120,121,0) 100%),
      linear-gradient(180deg, var(--back-light) 0%, #3c3c3d 30%, var(--back-mid) 55%, #1a1a1a 78%, var(--back-dark) 100%);
  }
  .card--front {
    left: 608px; top: 305px;
    background: var(--card);
    text-align: center;
    color: var(--text);
  }

  .brand-mark {
    position: absolute;
    left: 50%; top: 96px;
    width: 70px; height: 70px;
    margin-left: -35px;
    border-radius: 50%;
    background: var(--orange);
  }
  .brand-name {
    position: absolute; left: 0; right: 0; top: 213px;
    font-family: "Roboto Condensed", "Arial Narrow", sans-serif;
    font-weight: 500;
    font-size: 27px;
    color: var(--purple);
    line-height: 1;
  }
  .brand-tagline {
    position: absolute; left: 0; right: 0; top: 244px;
    font-family: "Roboto Condensed", "Arial Narrow", sans-serif;
    font-weight: 500;
    font-size: 8.5px;
    letter-spacing: 2px;
    text-transform: uppercase;
    color: var(--blue);
  }

  .person-name {
    position: absolute; left: 0; right: 0; top: 321px;
    font-size: 22px; font-weight: 500;
    color: var(--blue);
    letter-spacing: 0.3px;
  }
  .person-title {
    position: absolute; left: 0; right: 0; top: 353px;
    font-size: 15px; font-style: italic;
  }

  .contact-divider {
    position: absolute; left: 78px; top: 398px;
    width: 220px; height: 26px;
  }

  .contact-lines {
    position: absolute; left: 0; right: 0; top: 439px;
    font-size: 14.5px; line-height: 22px;
  }
  .address {
    position: absolute; left: 0; right: 0; top: 523px;
    font-size: 14.5px; line-height: 22px;
  }
</style>
</head>
<body>

<div class="card card--back" role="img" aria-label="Card back: large embossed brand monogram in grey and black tones"></div>

<div class="card card--front">
  <div class="brand-mark"></div>
  <div class="brand-name">Corven Behavioral Health</div>
  <div class="brand-tagline">Dedicated to hope, healing and recovery</div>

  <div class="person-name">MARTIN CORVEN</div>
  <div class="person-title">Managing Director</div>

  <svg class="contact-divider" viewBox="0 0 220 26" aria-hidden="true">
    <defs>
      <linearGradient id="ring" x1="0" y1="0" x2="1" y2="1">
        <stop offset="0" stop-color="#7a3a93"/>
        <stop offset="1" stop-color="#1a9ad6"/>
      </linearGradient>
    </defs>
    <line x1="0" y1="13" x2="58" y2="13" stroke="#7a3a93" stroke-width="1.5"/>
    <line x1="162" y1="13" x2="220" y2="13" stroke="#1a9ad6" stroke-width="1.5"/>
    <circle cx="84" cy="13" r="11" fill="none" stroke="url(#ring)" stroke-width="1.5"/>
    <path d="M78 10 q6 -5 12 0 l-2 2 -2 -1 -4 0 -2 1z M80 13 h8 l1 4 h-10z" fill="#1a9ad6"/>
    <circle cx="110" cy="13" r="11" fill="none" stroke="url(#ring)" stroke-width="1.5"/>
    <rect x="103.5" y="8.5" width="13" height="9" fill="none" stroke="#1a9ad6" stroke-width="1.3"/>
    <path d="M103.5 8.5 l6.5 5 6.5-5" fill="none" stroke="#1a9ad6" stroke-width="1.3"/>
    <circle cx="136" cy="13" r="11" fill="none" stroke="url(#ring)" stroke-width="1.5"/>
    <circle cx="136" cy="13" r="6" fill="none" stroke="#1a9ad6" stroke-width="1.2"/>
    <ellipse cx="136" cy="13" rx="2.6" ry="6" fill="none" stroke="#1a9ad6" stroke-width="1"/>
    <line x1="130" y1="13" x2="142" y2="13" stroke="#1a9ad6" stroke-width="1"/>
  </svg>

  <div class="contact-lines">
    000-111-0000<br>
    martin@corvenbehavioral.com<br>
    www.corvenbehavioral.com
  </div>
  <div class="address">
    123, Anywhere ST, Any City,<br>
    Any Town, US 123456
  </div>
</div>

</body>
</html>
```